USB Flash Drive Catalogue

I would like to make a paper catalogue of the products from our Quorvel store. There are currently 209 items on Quorvel. Some would be excluded. The listings have pricing and would need to be organized a bit different but all the information is there.

https://www.quorvel.com/shop/BrightPinStock/items?ref=pagination&page=1

Store

```html
<!DOCTYPE html>
<html lang="en">
<head>
<meta charset="utf-8">
<title>BrightPinStock Catalogue – Page 4</title>
<link href="https://fonts.googleapis.com/css2?family=Jost:wght@400;500;700&display=swap" rel="stylesheet">
<style>
  :root {
    --ink: #2a2a2a;
    --muted: #3c3c3c;
    --dot: #a8b6b6;
    --accent: #f28c38;
    --paper: #ffffff;
  }
  * { margin: 0; padding: 0; box-sizing: border-box; }
  html, body { width: 927px; height: 1200px; overflow: hidden; background: var(--paper); }
  body { font-family: "Jost", sans-serif; color: var(--ink); position: relative; }

  .brand { position: absolute; left: 30px; top: 28px; display: flex; align-items: center; gap: 8px; }
  .brand-mark { width: 22px; height: 22px; border-radius: 50%; background: var(--accent); }
  .brand-name { font-size: 21px; font-weight: 500; letter-spacing: 2px; color: var(--muted); }

  .catalogue { position: absolute; left: 50px; top: 92px; width: 823px; }
  .product {
    position: relative; height: 124px;
    border-top: 2px dotted var(--dot);
  }
  .catalogue .product:last-child { border-bottom: 2px dotted var(--dot); }
  .product-photo { position: absolute; left: 0; top: 9px; width: 132px; height: 106px; }

  .col { position: absolute; top: 9px; bottom: 6px; }
  .col + .col { border-left: 2px dotted var(--dot); }
  .col-desc { left: 136px; width: 404px; padding-left: 12px; border-left: 2px dotted var(--dot); }
  .col-size { left: 540px; width: 72px; text-align: center; }
  .col-material { left: 612px; width: 72px; text-align: center; }
  .col-color { left: 684px; width: 64px; text-align: center; }
  .col-capacity { left: 748px; width: 70px; text-align: center; }
  .col-price { left: 818px; width: 64px; text-align: center; border-left: 2px dotted var(--dot); }

  .col-head { font-size: 11.5px; font-weight: 500; letter-spacing: 0.6px; line-height: 14px; margin-bottom: 5px; }
  .col-body { font-size: 9.4px; line-height: 12.8px; color: var(--muted); }
  .col-body p + p { margin-top: 12.8px; }
  .col-size .col-body { font-size: 9px; }
  .list-stack { list-style: none; font-size: 9px; color: var(--muted); line-height: 19.6px; margin-top: -4px; }

  .speeds { position: absolute; left: 173px; top: 1088px; width: 620px; font-size: 9.4px; line-height: 12.8px; color: var(--muted); }
  .speeds h2 { font-size: 8.6px; font-weight: 700; font-variant: small-caps; letter-spacing: 0.3px; }
  .speeds-grid { display: grid; grid-template-columns: 327px 1fr; }

  .page-tab { position: absolute; left: 0; top: 1146px; width: 163px; height: 27px; background: var(--accent);
    color: #fff; font-size: 10px; font-weight: 700; display: flex; align-items: center; justify-content: flex-end; padding-right: 18px; }
</style>
</head>
<body>

<header class="brand">
  <span class="brand-mark"></span>
  <span class="brand-name">BrightPinStock</span>
</header>

<main class="catalogue">
  <!-- product rows -->
  <article class="product">
    <svg class="product-photo" role="img" aria-label="Product photo: walnut USB drive in open brown leather box"><rect width="132" height="106" fill="#fff"/><rect x="4" y="10" width="124" height="88" rx="4" fill="#7a3d28"/></svg>
    <div class="col col-desc"><h3 class="col-head">DESCRIPTION</h3><div class="col-body"><p>Walnut USB Flash Drive - Wildwood Body - Magnetic Cap - Packaged in<br>Elegant Brown PU Leather FLip Box - Printed “Mr &amp; Mrs” - Wooden USB.</p><p>High Quality Korvan Grade Chipset - Shock resistant and water proof<br>Chipset</p></div></div>
    <div class="col col-size"><h3 class="col-head">SIZE</h3><div class="col-body"><p>Leather Box<br>121x93x41 mm</p><p>Flash Drive<br>71x30x10 mm</p></div></div>
    <div class="col col-material"><h3 class="col-head">MATERIAL</h3><div class="col-body">Wood<br>(Walnut)</div></div>
    <div class="col col-color"><h3 class="col-head">COLOR</h3><div class="col-body">Medium<br>Brown</div></div>
    <div class="col col-capacity"><h3 class="col-head">CAPACITY</h3><ul class="list-stack"><li>16GB</li><li>32GB</li><li>64Gb</li><li>128GB</li></ul></div>
    <div class="col col-price"><h3 class="col-head">PRICE</h3><ul class="list-stack"><li>$24.95</li><li>$24.95</li><li>$24.95</li><li>$24.95</li></ul></div>
  </article>

  <article class="product">
    <svg class="product-photo" role="img" aria-label="Product photo: white wooden box with USB drive on dark wood surface"><rect width="132" height="106" fill="#3a3a3a"/><rect x="14" y="14" width="104" height="80" fill="#e6e3df"/></svg>
    <div class="col col-desc"><h3 class="col-head">DESCRIPTION</h3><div class="col-body"><p>Walnut USB Flash Drive - Wildwood Body - Magnetic Cap - Packaged in<br>Elegant Brown PU Leather FLip Box - Printed “Mr &amp; Mrs” - Wooden USB.</p><p>High Quality Korvan Grade Chipset - Shock resistant and water proof<br>Chipset</p></div></div>
    <div class="col col-size"><h3 class="col-head">SIZE</h3><div class="col-body"><p>Leather Box<br>121x93x41 mm</p><p>Flash Drive<br>71x30x10 mm</p></div></div>
    <div class="col col-material"><h3 class="col-head">MATERIAL</h3><div class="col-body">Wood<br>(Walnut)</div></div>
    <div class="col col-color"><h3 class="col-head">COLOR</h3><div class="col-body">Medium<br>Brown</div></div>
    <div class="col col-capacity"><h3 class="col-head">CAPACITY</h3><ul class="list-stack"><li>16GB</li><li>32GB</li><li>64Gb</li><li>128GB</li></ul></div>
    <div class="col col-price"><h3 class="col-head">PRICE</h3><ul class="list-stack"><li>$24.95</li><li>$24.95</li><li>$24.95</li><li>$24.95</li></ul></div>
  </article>

  <article class="product">
    <svg class="product-photo" role="img" aria-label="Product photo: light maple box with engraved wooden USB drive"><rect width="132" height="106" fill="#fff"/><rect x="6" y="14" width="120" height="80" fill="#e8d7b0"/></svg>
    <div class="col col-desc"><h3 class="col-head">DESCRIPTION</h3><div class="col-body"><p>Walnut USB Flash Drive - Wildwood Body - Magnetic Cap - Packaged in<br>Elegant Brown PU Leather FLip Box - Printed “Mr &amp; Mrs” - Wooden USB.</p><p>High Quality Korvan Grade Chipset - Shock resistant and water proof<br>Chipset</p></div></div>
    <div class="col col-size"><h3 class="col-head">SIZE</h3><div class="col-body"><p>Leather Box<br>121x93x41 mm</p><p>Flash Drive<br>71x30x10 mm</p></div></div>
    <div class="col col-material"><h3 class="col-head">MATERIAL</h3><div class="col-body">Wood<br>(Walnut)</div></div>
    <div class="col col-color"><h3 class="col-head">COLOR</h3><div class="col-body">Medium<br>Brown</div></div>
    <div class="col col-capacity"><h3 class="col-head">CAPACITY</h3><ul class="list-stack"><li>16GB</li><li>32GB</li><li>64Gb</li><li>128GB</li></ul></div>
    <div class="col col-price"><h3 class="col-head">PRICE</h3><ul class="list-stack"><li>$24.95</li><li>$24.95</li><li>$24.95</li><li>$24.95</li></ul></div>
  </article>

  <article class="product">
    <svg class="product-photo" role="img" aria-label="Product photo: white wooden box with USB drive on dark wood surface"><rect width="132" height="106" fill="#3a3a3a"/><rect x="14" y="14" width="104" height="80" fill="#e6e3df"/></svg>
    <div class="col col-desc"><h3 class="col-head">DESCRIPTION</h3><div class="col-body"><p>Walnut USB Flash Drive - Wildwood Body - Magnetic Cap - Packaged in<br>Elegant Brown PU Leather FLip Box - Printed “Mr &amp; Mrs” - Wooden USB.</p><p>High Quality Korvan Grade Chipset - Shock resistant and water proof<br>Chipset</p></div></div>
    <div class="col col-size"><h3 class="col-head">SIZE</h3><div class="col-body"><p>Leather Box<br>121x93x41 mm</p><p>Flash Drive<br>71x30x10 mm</p></div></div>
    <div class="col col-material"><h3 class="col-head">MATERIAL</h3><div class="col-body">Wood<br>(Walnut)</div></div>
    <div class="col col-color"><h3 class="col-head">COLOR</h3><div class="col-body">Medium<br>Brown</div></div>
    <div class="col col-capacity"><h3 class="col-head">CAPACITY</h3><ul class="list-stack"><li>16GB</li><li>32GB</li><li>64Gb</li><li>128GB</li></ul></div>
    <div class="col col-price"><h3 class="col-head">PRICE</h3><ul class="list-stack"><li>$24.95</li><li>$24.95</li><li>$24.95</li><li>$24.95</li></ul></div>
  </article>

  <article class="product">
    <svg class="product-photo" role="img" aria-label="Product photo: light blue wooden box with USB drive and straw filling"><rect width="132" height="106" fill="#fff"/><rect x="8" y="14" width="116" height="80" fill="#8fcbe6"/></svg>
    <div class="col col-desc"><h3 class="col-head">DESCRIPTION</h3><div class="col-body"><p>Walnut USB Flash Drive - Wildwood Body - Magnetic Cap - Packaged in<br>Elegant Brown PU Leather FLip Box - Printed “Mr &amp; Mrs” - Wooden USB.</p><p>High Quality Korvan Grade Chipset - Shock resistant and water proof<br>Chipset</p></div></div>
    <div class="col col-size"><h3 class="col-head">SIZE</h3><div class="col-body"><p>Leather Box<br>121x93x41 mm</p><p>Flash Drive<br>71x30x10 mm</p></div></div>
    <div class="col col-material"><h3 class="col-head">MATERIAL</h3><div class="col-body">Wood<br>(Walnut)</div></div>
    <div class="col col-color"><h3 class="col-head">COLOR</h3><div class="col-body">Medium<br>Brown</div></div>
    <div class="col col-capacity"><h3 class="col-head">CAPACITY</h3><ul class="list-stack"><li>16GB</li><li>32GB</li><li>64Gb</li><li>128GB</li></ul></div>
    <div class="col col-price"><h3 class="col-head">PRICE</h3><ul class="list-stack"><li>$24.95</li><li>$24.95</li><li>$24.95</li><li>$24.95</li></ul></div>
  </article>

  <article class="product">
    <svg class="product-photo" role="img" aria-label="Product photo: dark walnut box with USB drive and straw filling"><rect width="132" height="106" fill="#fff"/><rect x="6" y="12" width="120" height="84" fill="#5a2f1e"/></svg>
    <div class="col col-desc"><h3 class="col-head">DESCRIPTION</h3><div class="col-body"><p>Walnut USB Flash Drive - Wildwood Body - Magnetic Cap - Packaged in<br>Elegant Brown PU Leather FLip Box - Printed “Mr &amp; Mrs” - Wooden USB.</p><p>High Quality Korvan Grade Chipset - Shock resistant and water proof<br>Chipset</p></div></div>
    <div class="col col-size"><h3 class="col-head">SIZE</h3><div class="col-body"><p>Leather Box<br>121x93x41 mm</p><p>Flash Drive<br>71x30x10 mm</p></div></div>
    <div class="col col-material"><h3 class="col-head">MATERIAL</h3><div class="col-body">Wood<br>(Walnut)</div></div>
    <div class="col col-color"><h3 class="col-head">COLOR</h3><div class="col-body">Medium<br>Brown</div></div>
    <div class="col col-capacity"><h3 class="col-head">CAPACITY</h3><ul class="list-stack"><li>16GB</li><li>32GB</li><li>64Gb</li><li>128GB</li></ul></div>
    <div class="col col-price"><h3 class="col-head">PRICE</h3><ul class="list-stack"><li>$24.95</li><li>$24.95</li><li>$24.95</li><li>$24.95</li></ul></div>
  </article>

  <article class="product">
    <svg class="product-photo" role="img" aria-label="Product photo: black distressed wooden box with USB drive and straw filling"><rect width="132" height="106" fill="#fff"/><rect x="6" y="12" width="120" height="84" fill="#2e3234"/></svg>
    <div class="col col-desc"><h3 class="col-head">DESCRIPTION</h3><div class="col-body"><p>Walnut USB Flash Drive - Wildwood Body - Magnetic Cap - Packaged in<br>Elegant Brown PU Leather FLip Box - Printed “Mr &amp; Mrs” - Wooden USB.</p><p>High Quality Korvan Grade Chipset - Shock resistant and water proof<br>Chipset</p></div></div>
    <div class="col col-size"><h3 class="col-head">SIZE</h3><div class="col-body"><p>Leather Box<br>121x93x41 mm</p><p>Flash Drive<br>71x30x10 mm</p></div></div>
    <div class="col col-material"><h3 class="col-head">MATERIAL</h3><div class="col-body">Wood<br>(Walnut)</div></div>
    <div class="col col-color"><h3 class="col-head">COLOR</h3><div class="col-body">Medium<br>Brown</div></div>
    <div class="col col-capacity"><h3 class="col-head">CAPACITY</h3><ul class="list-stack"><li>16GB</li><li>32GB</li><li>64Gb</li><li>128GB</li></ul></div>
    <div class="col col-price"><h3 class="col-head">PRICE</h3><ul class="list-stack"><li>$24.95</li><li>$24.95</li><li>$24.95</li><li>$24.95</li></ul></div>
  </article>

  <article class="product">
    <svg class="product-photo" role="img" aria-label="Product photo: white printed wooden box with USB drive and straw filling"><rect width="132" height="106" fill="#fff"/><rect x="6" y="12" width="120" height="84" fill="#ebe8e2"/></svg>
    <div class="col col-desc"><h3 class="col-head">DESCRIPTION</h3><div class="col-body"><p>Walnut USB Flash Drive - Wildwood Body - Magnetic Cap - Packaged in<br>Elegant Brown PU Leather FLip Box - Printed “Mr &amp; Mrs” - Wooden USB.</p><p>High Quality Korvan Grade Chipset - Shock resistant and water proof<br>Chipset</p></div></div>
    <div class="col col-size"><h3 class="col-head">SIZE</h3><div class="col-body"><p>Leather Box<br>121x93x41 mm</p><p>Flash Drive<br>71x30x10 mm</p></div></div>
    <div class="col col-material"><h3 class="col-head">MATERIAL</h3><div class="col-body">Wood<br>(Walnut)</div></div>
    <div class="col col-color"><h3 class="col-head">COLOR</h3><div class="col-body">Medium<br>Brown</div></div>
    <div class="col col-capacity"><h3 class="col-head">CAPACITY</h3><ul class="list-stack"><li>16GB</li><li>32GB</li><li>64Gb</li><li>128GB</li></ul></div>
    <div class="col col-price"><h3 class="col-head">PRICE</h3><ul class="list-stack"><li>$24.95</li><li>$24.95</li><li>$24.95</li><li>$24.95</li></ul></div>
  </article>
</main>

<section class="speeds">
  <h2>Flash Drive average Read and Write Speed:</h2>
  <div class="speeds-grid">
    <p>16GB 2.0: read speed 30MB/S, write speed 11MB/S<br>64GB 3.0 : read speed 110MS/S, write speed 62MB/S</p>
    <p>32GB 3.0 : read speed 110MS/S, write speed 62MB/S<br>128GB 3.0: read speed 58MB/S, write speed 85MB/S</p>
  </div>
</section>

<footer class="page-tab">4</footer>

</body>
</html>
```